Letterhead, envelope & business card design

We would like to refresh the look and feel of our business cards & letterheads.

Our company specialises in premium property.

We are looking for a unique minimalist design for our letterhead & business cards that project this.

I can send over examples of our current design to draw from, although Im looking for some one with creativity, yet focussed on a clean modern, minimalist design.
Updates

I have just uploaded our current letterhead.

We have just removed the 'swoosh' grey symbol, but would still like to keep some part of grey in the design if possible.

thanks in advance.

Just uploaded my details for business card.

Can we see examples with the light grey used as the secondary color?

thanks in advance.

Target Market(s)

We are a premium real estate agency & we want that message to be carried through our business cards & stationery.

Industry/Entity Type

Business

```html
<!DOCTYPE html>
<html lang="en">
<head>
<meta charset="utf-8">
<title>Harwood Estate Agents – Stationery</title>
<link rel="stylesheet" href="https://fonts.googleapis.com/css2?family=Montserrat:wght@400;500&display=swap">
<style>
  :root {
    --brand-navy: #03475f;
    --paper: #f5f5f5;
    --backdrop: #e2e3e5;
    --ink-light: #ffffff;
  }
  * { margin: 0; padding: 0; box-sizing: border-box; }
  html, body { width: 1200px; height: 1001px; overflow: hidden; }
  body {
    position: relative;
    background: var(--backdrop);
    font-family: "Montserrat", Arial, sans-serif;
    color: var(--ink-light);
  }
  .letterhead {
    position: absolute; left: 181px; top: 58px;
    width: 607px; height: 860px;
    background: var(--paper);
  }
  .navy-block {
    position: absolute; left: 363px;
    width: 172px;
    background: var(--brand-navy);
  }
  .letterhead__header {
    top: 0; height: 157px;
    display: flex; align-items: center; justify-content: center;
  }
  .letterhead__footer {
    bottom: 0; height: 92px;
    display: flex; flex-direction: column; align-items: center; justify-content: center;
    text-align: center; font-size: 7.8px; line-height: 1.28;
  }
  .brand-name {
    font-size: 15px; font-weight: 500; line-height: 1.25;
    text-align: center;
  }
  .business-card {
    position: absolute; left: 360px;
    width: 175px; height: 217px;
    background: var(--brand-navy);
  }
  .business-card--front {
    top: 222px;
    display: flex; align-items: center; justify-content: center;
  }
  .business-card--back { top: 473px; }
  .business-card__web {
    position: absolute; left: 0; right: 0; bottom: 8px;
    text-align: center; font-size: 6.8px;
  }
  .business-card__name {
    position: absolute; left: 19px; top: 31px;
    font-size: 10.5px;
  }
  .business-card__contacts {
    position: absolute; left: 19px; bottom: 33px;
    font-size: 6.8px; line-height: 1.3;
  }
</style>
</head>
<body>
  <section class="letterhead" aria-label="Letterhead">
    <header class="navy-block letterhead__header">
      <p class="brand-name">Harwood<br>Estate Agents</p>
    </header>

    <section class="business-card business-card--front" aria-label="Business card front">
      <p class="brand-name">Harwood<br>Estate Agents</p>
      <p class="business-card__web">www.harwoodestates.com.au</p>
    </section>

    <section class="business-card business-card--back" aria-label="Business card back">
      <p class="business-card__name">Neil Harwood, Director</p>
      <div class="business-card__contacts">
        <p>Tel: (02) 5510 3420</p>
        <p>Fax: (02) 5510 3421</p>
        <p>Mob: 0455 207 619</p>
        <p>Email: neil@harwoodestates.com.au</p>
      </div>
    </section>

    <footer class="navy-block letterhead__footer">
      <p>58 Ridge Street,</p>
      <p>Marlow Bay NSW 2290</p>
      <p>Tel: (02) 5510 3420</p>
      <p>Fax: (02) 5510 3421</p>
      <p>Mob: 0455 207 619</p>
      <p>Email: neil@harwoodestates.com.au</p>
      <p>Web: www.harwoodestates.com.au</p>
    </footer>
  </section>
</body>
</html>
```